soft serve ice cream menu

I would like to rearrange my current menu board to more efficiently use space I have (42”W x 33”H) and change text to make it easier to read and understand. The business is a soft serve ice cream shop called Cone Haven in Lincolnwood IL. (www.conehavenicecream.example)

I have attached a picture of the current sign that i am replacing. Ideally, I would like to keep the basic red white and blue wavy line theme to match two other signs currently displayed. All of the prices need to be updated, and some other minor additions/ edits to be done.

I also have attached an excel file with what I have in mind In it, all updated prices are listed within three sections: basics, beverages, and fancy sundaes. There is one item (the Boston shake) that I tried to creatively put into both categories. I also tried to combine some ‘fancy sundae’ descriptions and prices to save room. That’s the extent of my creativity; it could use a lot more.
Thank you for your help!

• All descriptions of fancy sundaes from old sign

```html
<!DOCTYPE html>
<html lang="en">
<head>
<meta charset="utf-8">
<title>Cone Haven – Menu Board</title>
<link href="https://fonts.googleapis.com/css2?family=Anton&family=Arimo&family=Open+Sans:wght@400;600;700&family=Noto+Sans+Mono&display=swap" rel="stylesheet">
<style>
  :root{
    --red:#ff0000;
    --blue:#1a1aff;
    --blue-light:#3a3aff;
    --ink:#111;
    --row:#e4e4e4;
    --strip:#ececec;
    --tile-a:#b4b4b4;
    --tile-b:#c9c9c9;
    --tile-c:#d6d6d6;
    --tile-big:#bdbdbd;
    --price:#444;
    --white:#fff;
  }
  *{margin:0;padding:0;box-sizing:border-box}
  html,body{width:1200px;height:1003px;overflow:hidden;background:var(--white)}
  .board{position:relative;width:1200px;height:1003px;font-family:"Open Sans",Arial,sans-serif;color:var(--ink)}
  .banner-svg{position:absolute;left:0}
  .banner-title{position:absolute;font-family:"Anton",Impact,sans-serif;color:var(--white);font-size:40px;line-height:1;letter-spacing:-.3px;transform:scaleX(.88);transform-origin:left;white-space:nowrap}

  .tab{position:absolute;top:117px;height:18px;background:var(--red);color:var(--white);font-family:"Anton",Impact,sans-serif;font-size:14px;line-height:18px;text-align:center;letter-spacing:.3px}

  .row{position:absolute;background:var(--row)}
  .name{position:absolute;font-size:17px;line-height:1.1;white-space:nowrap}
  .name small{display:block;font-size:12px}
  .price{position:absolute;font-family:"Noto Sans Mono",monospace;font-size:17px;color:var(--price);text-align:center}
  .vline{position:absolute;top:135px;width:2px;height:453px;background:var(--ink)}
  .hline{position:absolute;height:2px;background:var(--ink)}
  .divider{position:absolute;left:596px;top:117px;width:10px;height:471px;background:var(--red)}

  .boston{position:absolute;left:0;top:590px;width:1200px;height:40px;background:var(--strip);font-size:16px}
  .boston-text{position:absolute;left:10px;top:9px;white-space:nowrap}
  .boston-name{position:absolute;left:906px;top:8px;font-weight:700;font-size:17px;text-decoration:underline;white-space:nowrap}
  .boston-sep{position:absolute;left:1062px;top:4px;width:2px;height:32px;background:var(--ink)}
  .boston-price{position:absolute;left:1074px;top:4px;font-family:"Noto Sans Mono",monospace;font-size:14px;line-height:15px;color:var(--price)}

  .tile{position:absolute;display:flex;align-items:center;justify-content:flex-end}
  .tile .t-name{font-weight:700;font-size:20px;text-align:right;line-height:1;white-space:nowrap}
  .tile .t-name small{display:block;font-weight:400;font-size:12px}
  .tile .t-price{font-family:"Noto Sans Mono",monospace;font-size:20px;color:var(--price);border-left:2px solid var(--ink);padding-left:4px;margin-left:4px;line-height:28px;white-space:nowrap}
  .a{background:var(--tile-a)} .b{background:var(--tile-b)} .c{background:var(--tile-c)}

  .split-desc{font-size:12px;text-align:center;line-height:1.2;font-weight:400}
  .big{position:absolute;left:892px;top:720px;width:308px;height:203px;background:var(--tile-big)}
  .big-text{position:absolute;left:4px;top:38px;width:224px;text-align:center}
  .big-text h3{font-size:18px;font-weight:700;white-space:nowrap}
  .big-text p{font-size:12px;line-height:1.1}
  .big-sep{position:absolute;left:233px;top:16px;width:2px;height:172px;background:var(--ink)}
  .big-price{position:absolute;left:238px;top:90px;font-family:"Noto Sans Mono",monospace;font-size:20px;color:var(--price)}

  .footer{position:absolute;left:0;top:930px;width:1200px;height:55px;background:linear-gradient(180deg,var(--blue-light),var(--blue));color:var(--white);font-family:"Arimo",Arial,sans-serif;font-size:21px;text-align:center;line-height:60px;white-space:nowrap}
</style>
</head>
<body>
<main class="board" aria-label="Cone Haven soft serve menu">

  <svg class="banner-svg" style="top:0" width="1200" height="125" viewBox="0 0 1200 125" aria-hidden="true">
    <defs>
      <linearGradient id="shadeTop" x1="0" y1="0" x2="0" y2="1">
        <stop offset="0" stop-color="#9a9a9a"/><stop offset="1" stop-color="#fafafa"/>
      </linearGradient>
    </defs>
    <path d="M0,88 C400,78 800,84 1200,100 V125 H0 Z" fill="url(#shadeTop)"/>
    <path d="M0,30 H1200 V108 C900,90 500,84 0,100 Z" fill="var(--red)"/>
  </svg>
  <div class="banner-title" style="left:218px;top:45px">THE BASICS</div>
  <div class="banner-title" style="left:826px;top:43px">BEVERAGES</div>

  <div class="tab" style="left:302px;width:96px">SMALL</div>
  <div class="tab" style="left:400px;width:96px">REGULAR</div>
  <div class="tab" style="left:498px;width:98px">LARGE</div>
  <div class="tab" style="left:877px;width:80px">SMALL</div>
  <div class="tab" style="left:959px;width:80px">REGULAR</div>
  <div class="tab" style="left:1041px;width:78px">LARGE</div>
  <div class="tab" style="left:1121px;width:79px">JUMBO</div>

  <div class="row" style="left:0;top:137px;width:596px;height:29px"></div>
  <div class="row" style="left:0;top:179px;width:596px;height:28px"></div>
  <div class="row" style="left:0;top:221px;width:596px;height:29px"></div>
  <div class="row" style="left:0;top:264px;width:596px;height:29px"></div>
  <div class="row" style="left:0;top:306px;width:596px;height:29px"></div>
  <div class="row" style="left:0;top:349px;width:596px;height:29px"></div>
  <div class="row" style="left:0;top:391px;width:596px;height:29px"></div>
  <div class="row" style="left:0;top:434px;width:596px;height:29px"></div>
  <div class="row" style="left:0;top:476px;width:596px;height:29px"></div>
  <div class="row" style="left:0;top:519px;width:596px;height:29px"></div>
  <div class="row" style="left:0;top:560px;width:596px;height:28px"></div>
  <div class="row" style="left:606px;top:137px;width:594px;height:29px"></div>
  <div class="row" style="left:606px;top:179px;width:594px;height:28px"></div>
  <div class="row" style="left:606px;top:221px;width:594px;height:29px"></div>
  <div class="row" style="left:606px;top:264px;width:594px;height:29px"></div>
  <div class="row" style="left:606px;top:306px;width:594px;height:29px"></div>
  <div class="row" style="left:606px;top:348px;width:594px;height:48px"></div>
  <div class="row" style="left:606px;top:411px;width:594px;height:50px"></div>
  <div class="row" style="left:606px;top:476px;width:594px;height:29px"></div>
  <div class="row" style="left:606px;top:519px;width:594px;height:29px"></div>
  <div class="row" style="left:606px;top:560px;width:594px;height:28px"></div>

  <div class="hline" style="left:0;top:134px;width:1200px"></div>
  <div class="hline" style="left:0;top:587px;width:1200px"></div>
  <div class="vline" style="left:300px"></div>
  <div class="vline" style="left:398px"></div>
  <div class="vline" style="left:496px"></div>
  <div class="vline" style="left:875px"></div>
  <div class="vline" style="left:957px"></div>
  <div class="vline" style="left:1039px"></div>
  <div class="vline" style="left:1119px"></div>
  <div class="divider"></div>

  <div class="name" style="left:10px;top:143px">Cones</div>
  <div class="name" style="left:10px;top:183px">Dipped (or Flavor Swirl)</div>
  <div class="name" style="left:10px;top:227px">Snow Blitzs</div>
  <div class="name" style="left:10px;top:270px">Sundaes</div>
  <div class="name" style="left:10px;top:312px">Cups</div>
  <div class="name" style="left:10px;top:355px">Funnel Cake</div>
  <div class="name" style="left:10px;top:397px">Frozen Banana</div>
  <div class="name" style="left:10px;top:440px">Buddy Bar</div>
  <div class="name" style="left:10px;top:482px">Frozen Bar</div>
  <div class="name" style="left:10px;top:525px">Chocolate Chip Sandwhich</div>

  <div class="price" style="left:302px;width:96px;top:141px">2,25</div>
  <div class="price" style="left:400px;width:96px;top:141px">2,75</div>
  <div class="price" style="left:498px;width:98px;top:141px">3,35</div>
  <div class="price" style="left:302px;width:96px;top:182px">2,6</div>
  <div class="price" style="left:400px;width:96px;top:182px">3,1</div>
  <div class="price" style="left:498px;width:98px;top:182px">3,9</div>
  <div class="price" style="left:302px;width:96px;top:225px">4,3</div>
  <div class="price" style="left:400px;width:96px;top:225px">5,35</div>
  <div class="price" style="left:498px;width:98px;top:225px">6,5</div>
  <div class="price" style="left:302px;width:96px;top:267px">3,1</div>
  <div class="price" style="left:400px;width:96px;top:267px">3,95</div>
  <div class="price" style="left:498px;width:98px;top:267px">5,6</div>
  <div class="price" style="left:302px;width:96px;top:310px">1,9</div>
  <div class="price" style="left:400px;width:96px;top:310px">2,55</div>
  <div class="price" style="left:498px;width:98px;top:310px">3,4</div>
  <div class="price" style="left:400px;width:96px;top:352px">2,25</div>
  <div class="price" style="left:400px;width:96px;top:394px">2,25</div>
  <div class="price" style="left:400px;width:96px;top:437px">2,25</div>
  <div class="price" style="left:400px;width:96px;top:479px">1,95</div>
  <div class="price" style="left:400px;width:96px;top:522px">2,25</div>

  <div class="name" style="left:621px;top:143px">Milkshakes</div>
  <div class="name" style="left:621px;top:184px">Malts</div>
  <div class="name" style="left:621px;top:227px">Ice Cream Soda</div>
  <div class="name" style="left:621px;top:270px">Phosphates</div>
  <div class="name" style="left:621px;top:312px">Root Beer Floats</div>
  <div class="name" style="left:621px;top:355px">Floats<small>(kola, orange dream, green meadow)</small></div>
  <div class="name" style="left:619px;top:418px">Yogurt Fruit Smoothies<small>(strawberry, strawberry/banana, pineapple)</small></div>
  <div class="name" style="left:621px;top:482px">Ice Slushies</div>
  <div class="name" style="left:621px;top:525px">Slushie Freeze</div>
  <div class="name" style="left:621px;top:565px">Slushie Float</div>

  <div class="price" style="left:959px;width:80px;top:141px">3,4</div>
  <div class="price" style="left:1041px;width:78px;top:141px">4,5</div>
  <div class="price" style="left:1121px;width:79px;top:141px">7,25</div>
  <div class="price" style="left:959px;width:80px;top:182px">3,65</div>
  <div class="price" style="left:1041px;width:78px;top:182px">4,85</div>
  <div class="price" style="left:1121px;width:79px;top:182px">7,85</div>
  <div class="price" style="left:959px;width:80px;top:225px">3,4</div>
  <div class="price" style="left:1041px;width:78px;top:225px">4,5</div>
  <div class="price" style="left:1121px;width:79px;top:225px">7,25</div>
  <div class="price" style="left:959px;width:80px;top:267px">3,1</div>
  <div class="price" style="left:1041px;width:78px;top:267px">4,25</div>
  <div class="price" style="left:1121px;width:79px;top:267px">6,65</div>
  <div class="price" style="left:959px;width:80px;top:310px">3,25</div>
  <div class="price" style="left:1041px;width:78px;top:310px">4,45</div>
  <div class="price" style="left:1121px;width:79px;top:310px">6,85</div>
  <div class="price" style="left:959px;width:80px;top:360px">3,25</div>
  <div class="price" style="left:1041px;width:78px;top:360px">4,45</div>
  <div class="price" style="left:1121px;width:79px;top:360px">6,85</div>
  <div class="price" style="left:877px;width:80px;top:425px">4,25</div>
  <div class="price" style="left:959px;width:80px;top:425px">5,65</div>
  <div class="price" style="left:1041px;width:78px;top:425px">7,85</div>
  <div class="price" style="left:959px;width:80px;top:479px">2,25</div>
  <div class="price" style="left:1041px;width:78px;top:479px">2,85</div>
  <div class="price" style="left:1121px;width:79px;top:479px">5,05</div>
  <div class="price" style="left:959px;width:80px;top:522px">3,5</div>
  <div class="price" style="left:1041px;width:78px;top:522px">4,6</div>
  <div class="price" style="left:1121px;width:79px;top:522px">7,35</div>
  <div class="price" style="left:959px;width:80px;top:562px">3,5</div>
  <div class="price" style="left:1041px;width:78px;top:562px">4,6</div>
  <div class="price" style="left:1121px;width:79px;top:562px">7,35</div>

  <section class="boston">
    <div class="boston-text">(The perfect solution to the sundae/ shake decision ) A milkshake of your choice topped with the sundae of your choice.</div>
    <div class="boston-name">The Boston Shake</div>
    <div class="boston-sep"></div>
    <div class="boston-price">Large 6,15<br>Jumbo 10,80</div>
  </section>

  <svg class="banner-svg" style="top:630px" width="1200" height="90" viewBox="0 0 1200 90" aria-hidden="true">
    <defs>
      <linearGradient id="shadeMid" x1="0" y1="0" x2="0" y2="1">
        <stop offset="0" stop-color="#333"/><stop offset=".5" stop-color="#9a9a9a"/><stop offset="1" stop-color="#f2f2f2"/>
      </linearGradient>
    </defs>
    <path d="M0,58 C400,52 800,50 1200,60 V88 H0 Z" fill="url(#shadeMid)"/>
    <path d="M0,2 H1200 V66 C850,52 450,50 0,66 Z" fill="var(--red)"/>
  </svg>
  <div class="banner-title" style="left:483px;top:641px">FANCY SUNDAES</div>

  <div class="tile a" style="left:0;top:720px;width:306px;height:47px;padding-right:72px"><span class="t-name">Turtle</span><span class="t-price">5,65</span></div>
  <div class="tile a" style="left:0;top:772px;width:306px;height:47px;padding-right:72px"><span class="t-name">Velvet</span><span class="t-price">6,25</span></div>
  <div class="tile a" style="left:0;top:824px;width:306px;height:47px;padding-right:72px"><span class="t-name">Pina Colada</span><span class="t-price">5,65</span></div>
  <div class="tile a" style="left:0;top:876px;width:306px;height:47px;padding-right:72px"><span class="t-name">Parfait<small>(original or buddy)</small></span><span class="t-price">5,65</span></div>

  <div class="tile b" style="left:308px;top:720px;width:286px;height:47px;padding-right:50px"><span class="t-name">Brownie</span><span class="t-price">6,25</span></div>
  <div class="tile b" style="left:308px;top:772px;width:286px;height:47px;padding-right:50px"><span class="t-name">Rocky Rock</span><span class="t-price">5,65</span></div>
  <div class="tile b" style="left:308px;top:824px;width:286px;height:47px;padding-right:50px"><span class="t-name">Funnel Cake</span><span class="t-price">7,50</span></div>
  <div class="tile b" style="left:308px;top:876px;width:286px;height:47px;padding-right:50px"><span class="t-name">Cup Split</span><span class="t-price">8,25</span></div>

  <div class="tile c" style="left:606px;top:720px;width:284px;height:47px;padding-right:6px"><span class="t-name" style="font-size:19px">Double Fudge<small>(topped with pecans)</small></span><span class="t-price">&nbsp;5,65</span></div>
  <div class="tile c" style="left:606px;top:772px;width:284px;height:99px;padding-right:12px">
    <span class="t-name" style="font-size:19px">Banana Split<span class="split-desc" style="display:block;margin-top:2px">(fudge split - hold the strawberries<br>pineapple and drench<br>with hot fudge - 8.00)</span></span>
    <span class="t-price" style="line-height:80px;padding-left:10px">7,5</span>
  </div>
  <div class="tile c" style="left:606px;top:876px;width:284px;height:47px;padding-right:6px"><span class="t-name" style="font-size:19px">Strawberry Shortcake</span><span class="t-price">&nbsp;5,85</span></div>

  <div class="big">
    <div class="big-text">
      <h3>The Super Jumbo B-Split</h3>
      <p>Warning: not recommended to be eaten without parental supervision. Over twice the size as the original with two sliced bananas topped off with a large mound of strawberry ice cream in the center. If you’re hungry enough to order this, you’ll be happy to know its too large to prepare to-go.</p>
    </div>
    <div class="big-sep"></div>
    <div class="big-price">15,95</div>
  </div>

  <footer class="footer">Fat free Yogurt, Premium Cholov Yisroel, and Non-Dairy Vegan soft serve prices listed inside</footer>
</main>
</body>
</html>
```